Retail Jewelry Business Card Design Project

We are in need of a new business card design for a retail jewelry store. This store is in the business of fine jewelry including but not specific to bridal jewelry, diamonds, designer jewelry and watches.

This store has been in business for 20 years but continues to strive for a modern professional appeal. The main colors use for this business are a royal blue, white and silver.

Target Market(s)

Target market is ages 18-50

Industry/Entity Type

Jewelry

Requirements
Must have
• Sales Person Name
Sales Person Email Address

Store Address
Store Phone
Website

Standard business card size. No odd shapes or sizes.
Nice to have
• Overall modern feel for card.

We have thought that a design with a nice feature of the logo on the back of the card would be nice but open to ideas.
Should not have
• No specific images of jewelry should be used.

```html
<!DOCTYPE html>
<html lang="en">
<head>
<meta charset="utf-8">
<title>Everett Lane Fine Jewelry – Business Card</title>
<link rel="stylesheet" href="https://fonts.googleapis.com/css2?family=Cinzel:wght@400;600&family=Didact+Gothic&display=swap">
<style>
  :root {
    --backdrop: #c3c0b2;
    --royal: #2e2b8c;
    --royal-soft: #5a56a8;
    --ink: #2a2a2e;
    --white: #ffffff;
    --silver-1: #e4e5e9;
    --silver-2: #f7f7f9;
    --silver-3: #d9dadf;
  }
  * { box-sizing: border-box; margin: 0; padding: 0; }
  html, body { width: 1200px; height: 900px; overflow: hidden; }
  body { background: var(--backdrop); position: relative; font-family: "Didact Gothic", sans-serif; }

  .card {
    position: absolute;
    background: linear-gradient(120deg, var(--silver-1) 0%, var(--silver-2) 30%, var(--silver-3) 55%, var(--silver-2) 75%, var(--silver-1) 100%);
  }
  .card__panel {
    position: absolute;
    background: var(--white);
    display: flex;
    flex-direction: column;
    align-items: center;
    justify-content: center;
  }

  .card--front { left: 475px; top: 58px; width: 656px; height: 378px; }
  .card--front .card__panel { left: 28px; top: 28px; width: 599px; height: 324px; border: 1px solid #dcdde1; }

  .brand {
    font-family: "Cinzel", serif;
    font-weight: 600;
    color: var(--royal);
    font-size: 50px;
    letter-spacing: 1px;
    text-align: center;
    line-height: 1.15;
    margin-top: -6px;
  }
  .brand span { display: block; font-size: 22px; letter-spacing: 3px; margin-top: 8px; }

  .card--back { left: 63px; top: 460px; width: 658px; height: 379px; }
  .card--back .card__panel { left: 29px; top: 27px; width: 600px; height: 323px; }

  .contact { text-align: center; width: 300px; }
  .contact__name {
    font-family: "Cinzel", serif;
    color: var(--royal);
    font-size: 21px;
    letter-spacing: 2.5px;
    margin-bottom: 8px;
  }
  .contact__email { color: var(--ink); font-size: 15.5px; letter-spacing: 1.2px; }
  .contact__rule { height: 1px; background: var(--royal-soft); margin: 16px 0 12px; }
  .contact__address { color: var(--ink); font-size: 17px; line-height: 27px; font-style: normal; }
  .contact__web { color: var(--royal); font-size: 15.5px; letter-spacing: 0.6px; }
</style>
</head>
<body>
  <section class="card card--front" aria-label="Card front">
    <div class="card__panel">
      <p class="brand">Everett Lane<span>Fine Jewelry</span></p>
    </div>
  </section>

  <section class="card card--back" aria-label="Card back">
    <div class="card__panel">
      <div class="contact">
        <p class="contact__name">Marcus Everett Lane</p>
        <p class="contact__email">marcus@everettlanejewelry.com</p>
        <div class="contact__rule"></div>
        <address class="contact__address">2280 Marlowe Avenue<br>Bayport, FL 32099<br>(850) 555-0142</address>
        <div class="contact__rule"></div>
        <p class="contact__web">www.everettlanejewelry.com</p>
      </div>
    </div>
  </section>
</body>
</html>
```